Website for International Non-Profit for Birth Parent Searching

Tulo Link is a 501(c)(3) non-profit organization that helps Chinese adoptees search and reunite with birth families who were separated due the One Child Policy in China. We want to create a website that can link to an information database that allows website users to easily access information around search ads in an organized way; help connect families to professional searchers; provide resources for community support for adoptees and their families as they embark on a personal and emotional journey of finding birth family through support groups on social media and consultation/education on the searching process; and provide the opportunity for the adoptive community to give back through donations and volunteer opportunities. The final design should foster a sense of community and be easy navigable to access the multiple resources we provide to help families search for each other. We would like to see designs with red/black/white color schemes that are gentle, inviting, and family friendly to viewers. We would like to see some design layouts with Chinese themes, if possible.

```html
<!DOCTYPE html>
<html lang="en">
<head>
<meta charset="UTF-8">
<title>Tulo Link – International Non-Profit for Birth Parent Searching</title>
<link href="https://fonts.googleapis.com/css2?family=Red+Hat+Display:wght@500;700;800;900&family=Lato:ital,wght@0,400;0,700;0,900;1,400&display=swap" rel="stylesheet">
<style>
:root{
  --red:#a3060e;
  --red-dark:#7d0309;
  --ink:#1a1a1a;
  --text:#4a4a4a;
  --grey:#ececec;
  --light:#f3f3f3;
  --white:#ffffff;
  --star:#e2930a;
}
*{box-sizing:border-box;margin:0;padding:0}
html,body{width:1200px;height:4792px;overflow:hidden;background:var(--white)}
body{font-family:"Lato",sans-serif;color:var(--text)}
.page{position:relative;width:1200px;height:4792px;overflow:hidden}
.abs{position:absolute}
h1,h2,h3,.head{font-family:"Red Hat Display",sans-serif;color:var(--ink)}
.btn{position:absolute;display:flex;align-items:center;justify-content:center;font-family:"Red Hat Display",sans-serif;font-weight:800;font-size:15px;text-transform:uppercase;letter-spacing:.2px}
.btn-red{background:var(--red);color:var(--white);box-shadow:0 3px 6px rgba(0,0,0,.25)}
.btn-white{background:var(--white);color:var(--ink)}
.btn-outline{border:2px solid var(--white);color:var(--white)}

/* header */
.site-header{position:absolute;left:0;top:0;width:1200px;height:89px;background:var(--white)}
.logo{position:absolute;left:143px;top:20px;font-family:"Red Hat Display",sans-serif;font-weight:900;font-size:34px;color:var(--ink);white-space:nowrap}
.nav{position:absolute;left:366px;top:32px;display:flex;gap:27px;font-family:"Red Hat Display",sans-serif;font-weight:700;font-size:15px;color:var(--ink)}
.nav .active{color:var(--red)}

/* hero */
.hero-photo{left:0;top:89px;width:1200px;height:720px;background:linear-gradient(100deg,#6d7b4e 0%,#8c9a62 30%,#c9b79a 55%,#a89070 75%,#5e6d3f 100%)}
.hero-title{left:143px;top:208px;font-size:51px;line-height:62px;font-weight:800;color:var(--white);width:400px}

/* feature circles */
.feature{position:absolute;border-radius:50%;text-align:center;display:flex;flex-direction:column;align-items:center}
.feature h3{font-size:17px;font-weight:800;margin:8px 0 10px}
.feature p{font-size:14px;line-height:20px}
.feature-grey{background:var(--grey);width:286px;height:286px;padding-top:36px}
.feature-grey p{width:210px;color:#333}
.feature-red{background:var(--red);border:9px solid var(--white);width:366px;height:366px;padding-top:40px;color:var(--white);box-shadow:0 2px 10px rgba(0,0,0,.2)}
.feature-red h3{color:var(--white);font-size:19px}
.feature-red p{width:240px;font-weight:700}

/* welcome */
.section-title{left:0;width:1200px;text-align:center;font-weight:800;font-size:40px}
.welcome-text{left:180px;top:1094px;width:840px;text-align:center;font-size:15.5px;line-height:24px}

/* organized */
.org-photo{left:520px;top:1395px;width:680px;height:558px;background:linear-gradient(120deg,#5a2a20 0%,#8a4636 35%,#c7977c 55%,#8b1a1a 80%,#5a0f10 100%)}
.org-title{left:143px;top:1458px;font-size:39px;font-weight:800;color:var(--white)}
.org-list{left:143px;top:1535px;width:400px;list-style:none;color:var(--white);font-size:15.5px;line-height:24px}
.org-list li{position:relative;padding-left:28px;margin-bottom:12px}
.org-list li svg{position:absolute;left:0;top:5px}

/* news */
.card{position:absolute;background:var(--white);box-shadow:0 0 10px rgba(0,0,0,.14)}
.date{position:absolute;background:var(--red);color:var(--white);font-family:"Red Hat Display",sans-serif;font-weight:800;font-size:11.5px;line-height:12px;text-align:center;padding:4px 7px}
.news-head{font-family:"Red Hat Display",sans-serif;font-weight:800;font-size:13.5px;line-height:24px;color:var(--ink);text-transform:uppercase}
.news-body{font-size:12.5px;line-height:17px;color:#444}
.more{font-family:"Red Hat Display",sans-serif;font-weight:800;font-size:12.5px;color:var(--ink);display:flex;align-items:center;gap:6px}

/* birth parent */
.bp-photo{left:0;top:2786px;width:1200px;height:549px;background:linear-gradient(110deg,#3e4a30 0%,#6b6a4e 30%,#9a8672 45%,#4f5b39 70%,#2e3a22 100%)}
.bp-card{left:651px;top:2894px;width:465px;height:337px;background:var(--white);border-left:6px solid var(--red);padding:42px 36px 0 34px}
.bp-card h2{font-size:33px;line-height:38px;font-weight:800}
.bp-card p{margin-top:14px;font-size:15px;line-height:22px;color:#444}

/* testimonials */
.clients{left:0;top:3335px;width:1200px;height:640px;background:var(--light)}
.quote{position:absolute;background:var(--white);border-radius:14px;box-shadow:0 4px 12px rgba(0,0,0,.1);width:411px;height:247px;padding:36px 44px}
.quote p{font-style:italic;font-size:15px;line-height:23px;color:#444;position:relative}
.stars{color:var(--star);font-size:17px;letter-spacing:2px;margin-top:14px}
.avatar{position:absolute;width:90px;height:90px;border-radius:50%;background:radial-gradient(circle,#b79b80 0%,#6f7f52 70%)}
.person{position:absolute;font-family:"Red Hat Display",sans-serif;font-weight:800;font-size:12px;line-height:22px;color:var(--ink)}
.slider-arrow{position:absolute;z-index:2}

/* join */
.join-photo{left:0;top:3950px;width:1200px;height:421px;background:linear-gradient(100deg,#7b0208 0%,#a3101a 40%,#b42a2a 60%,#8a050c 100%)}
.join-title{left:0;top:4080px;width:1200px;text-align:center;font-size:32px;font-weight:800;color:var(--white)}
.field{position:absolute;height:45px;border:1.5px solid var(--white);color:var(--white);font-size:14px;display:flex;align-items:center;padding-left:22px}

/* contact */
.contact-col{position:absolute;top:4405px;text-align:center}
.contact-col h4{font-family:"Red Hat Display",sans-serif;font-weight:800;font-size:15px;color:var(--ink);margin-top:14px}
.contact-col p{font-size:14.5px;line-height:20px;color:#333;margin-top:4px}
.divider{position:absolute;top:4371px;width:1px;height:214px;background:#ddd}
.footer-links{left:0;top:4628px;width:1200px;text-align:center;font-size:15px;color:var(--ink)}
.copyright{left:0;top:4664px;width:1200px;text-align:center;font-size:15px;color:var(--ink)}
.social{position:absolute;top:4710px;width:34px;height:34px;border-radius:50%;border:2px solid var(--red)}
</style>
</head>
<body>
<div class="page">

  <header class="site-header">
    <div class="logo">Tulo Link</div>
    <nav class="nav">
      <span class="active">HOME</span><span>MISSION</span><span>VISION</span><span>ABOUT US</span><span>BLOG</span><span>CONTACT US</span>
    </nav>
    <div class="btn btn-red" style="left:898px;top:20px;width:157px;height:42px;font-size:14px">Donate Now</div>
  </header>

  <div class="abs hero-photo" role="img" aria-label="Photo of a smiling family outdoors, a child on his father's shoulders and a mother pointing to the sky"></div>
  <h1 class="abs hero-title">International Non-Profit for Birth Parent Searching</h1>
  <div class="btn btn-white" style="left:143px;top:472px;width:183px;height:45px">Serach Ads</div>
  <div class="btn btn-red" style="left:348px;top:472px;width:179px;height:45px">Connect</div>
  <svg class="abs" style="left:0;top:640px" width="1200" height="180" viewBox="0 0 1200 180">
    <path d="M0,162 C380,150 820,125 1200,58 L1200,180 L0,180 Z" fill="#ffffff"/>
    <path d="M0,146 C140,124 290,112 420,118 C290,128 140,150 0,168 Z" fill="#a3060e"/>
  </svg>

  <div class="feature feature-grey" style="left:142px;top:666px">
    <svg width="64" height="60" viewBox="0 0 64 60" fill="none" stroke="#a3060e" stroke-width="3">
      <rect x="6" y="6" width="52" height="48" rx="6"/><circle cx="20" cy="22" r="6"/><circle cx="44" cy="22" r="6"/><path d="M10 46c2-8 18-8 20 0M34 46c2-8 18-8 20 0"/>
    </svg>
    <h3 class="head">MISSION</h3>
    <p>Sed ut perspiciatis unde omnis iste natus voluptatem accuntium doloremque laudantium, totam rem aperiam, eaque</p>
    <svg style="margin-top:14px" width="26" height="20" viewBox="0 0 26 20"><path d="M2 10h20M14 3l8 7-8 7" stroke="#333" stroke-width="3" fill="none"/></svg>
  </div>
  <div class="feature feature-red" style="left:416px;top:598px">
    <svg width="80" height="80" viewBox="0 0 80 80" fill="none" stroke="#fff" stroke-width="3">
      <circle cx="40" cy="36" r="10"/><path d="M40 30v12M36 33h6a3 3 0 010 6h-4"/><path d="M8 52l14-6h18l-2 8H26M8 64l18 4 36-16-6-6-16 8"/><path d="M46 18l18-12 8 10-18 12z"/>
    </svg>
    <h3 class="head">DONATIONS</h3>
    <p>Sed ut perspiciatis unde omnis iste natus voluptatem accutium doloremque laudantium, totam rem aperiam, eaque ipsa</p>
    <div class="btn btn-outline" style="position:relative;margin-top:18px;width:134px;height:42px;font-size:13px">Learn More</div>
  </div>
  <div class="feature feature-grey" style="left:770px;top:666px">
    <svg width="64" height="60" viewBox="0 0 64 60" fill="none" stroke="#a3060e" stroke-width="3">
      <rect x="14" y="4" width="36" height="26" rx="3"/><path d="M20 24l8-8 6 6 10-10"/><circle cx="12" cy="40" r="5"/><circle cx="32" cy="40" r="5"/><circle cx="52" cy="40" r="5"/><path d="M4 56c2-7 14-7 16 0M24 56c2-7 14-7 16 0M44 56c2-7 14-7 16 0"/>
    </svg>
    <h3 class="head">VISION</h3>
    <p>Sed ut perspiciatis unde omnis iste natus error sit voluptatem accuntium doloremque laudantium, totam rem aperiam, eaque</p>
    <svg style="margin-top:14px" width="26" height="20" viewBox="0 0 26 20"><path d="M2 10h20M14 3l8 7-8 7" stroke="#333" stroke-width="3" fill="none"/></svg>
  </div>

  <h2 class="abs section-title" style="top:1028px">WELCOME TO TULO LINK</h2>
  <p class="abs welcome-text">Sed ut perspiciatis unde omnis iste natus error sit voluptatem accusantium doloremque laudantium, totam rem aperiam, eaque ipsa quae ab illo inventore veritatis et quasi architecto beatae vitae dicta sunt explicabo. Nemo enim ipsam voluptatem quia voluptas sit aspernatur aut odit aut fugit, sed quia consequuntur magni dolores eos qui ratione voluptatem sequi nesciunt. Neque porro quisquam est, qui dolorem ipsum quia dolor sit amet, consectetur, adipisci velit, sed quia non numquam eius modi tempora incidunt ut labore et dolore magnam aliquam quaerat voluptatem. Ut enim ad minima veniam, quis nostrum exercitationem ullam</p>
  <div class="btn btn-red" style="left:519px;top:1267px;width:162px;height:43px">Learn More</div>

  <div class="abs org-photo" role="img" aria-label="Photo of a grandfather guiding a young child's hand as he paints Chinese calligraphy"></div>
  <svg class="abs" style="left:0;top:1395px" width="620" height="558" viewBox="0 0 620 558" role="img" aria-label="Deep red fabric texture background">
    <defs><linearGradient id="silk" x1="0" y1="0" x2="1" y2="1"><stop offset="0" stop-color="#a30a12"/><stop offset=".5" stop-color="#b8111a"/><stop offset="1" stop-color="#8e060d"/></linearGradient></defs>
    <path d="M0,0 H560 C610,180 600,380 520,558 H0 Z" fill="url(#silk)"/>
  </svg>
  <h2 class="abs org-title">ORGANIZED WAY</h2>
  <ul class="abs org-list">
    <li><svg width="14" height="14" viewBox="0 0 14 14"><circle cx="7" cy="7" r="7" fill="#fff"/><path d="M5 4l3 3-3 3" stroke="#a3060e" stroke-width="2" fill="none"/></svg>Help Connect Families To Professional Searchers</li>
    <li><svg width="14" height="14" viewBox="0 0 14 14"><circle cx="7" cy="7" r="7" fill="#fff"/><path d="M5 4l3 3-3 3" stroke="#a3060e" stroke-width="2" fill="none"/></svg>Provide Resources For Community Support For Adoptees And Their Families As They Embark On A Personal And Emotional Journey Of Finding Birth Family Through Support Groups On Social Media And Consultation/education On The Searching Process</li>
    <li><svg width="14" height="14" viewBox="0 0 14 14"><circle cx="7" cy="7" r="7" fill="#fff"/><path d="M5 4l3 3-3 3" stroke="#a3060e" stroke-width="2" fill="none"/></svg>And Provide The Opportunity For The Adoptive Community To Give Back Through Donations And Volunteer Opportunitie</li>
  </ul>
  <div class="btn btn-outline" style="left:143px;top:1823px;width:164px;height:42px">Learn More</div>

  <h2 class="abs section-title" style="top:2018px">RECENT NEWS</h2>
  <div class="card" style="left:143px;top:2113px;width:480px;height:580px">
    <div class="abs" style="left:0;top:0;width:480px;height:368px;background:linear-gradient(120deg,#c98a3a,#e4b160 40%,#b9a58a 70%,#7a5a2e)" role="img" aria-label="Photo of a laughing girl playing airplane with her father among autumn trees"></div>
    <div class="date" style="left:24px;top:408px">APRI 17<br>2021</div>
    <div class="news-head abs" style="left:97px;top:402px;width:360px;line-height:20px">Sed ut perspiciatis unde omnis iste voluptatem accusantium doloremque lauda</div>
    <p class="news-body abs" style="left:22px;top:460px;width:410px">Sed ut perspiciatis unde omnis iste natus error sit voluptatem acctium doloremque laudantium, totam rem aperiam, eaque ipsa quae ab illo inventore veritatis et quasi architecto beatae vitae</p>
    <div class="more abs" style="left:22px;top:530px">LEARN MORE <svg width="14" height="10" viewBox="0 0 14 10"><path d="M1 5h11M8 1l4 4-4 4" stroke="#a3060e" stroke-width="2" fill="none"/></svg></div>
  </div>

  <div class="card" style="left:651px;top:2113px;width:402px;height:184px">
    <div class="abs" style="left:0;top:0;width:171px;height:184px;background:linear-gradient(135deg,#5a6f8e,#b87a4a 60%,#7a5a3e)" role="img" aria-label="Photo of a toddler climbing on a playground"></div>
    <div class="date" style="left:118px;top:24px">APRI 17<br>2021</div>
    <div class="news-head abs" style="left:198px;top:20px;width:190px">Nemo enim ipsam voluptatem quiasit</div>
    <p class="news-body abs" style="left:200px;top:80px;width:180px">Sed ut perspiciatis unde omnis iste natus error sit voluptatem accusantium doloremque</p>
    <div class="more abs" style="left:200px;top:140px">LEARN MORE <svg width="14" height="10" viewBox="0 0 14 10"><path d="M1 5h11M8 1l4 4-4 4" stroke="#a3060e" stroke-width="2" fill="none"/></svg></div>
  </div>
  <div class="card" style="left:651px;top:2314px;width:402px;height:184px">
    <div class="abs" style="left:0;top:0;width:171px;height:184px;background:linear-gradient(135deg,#8fa86a,#c0b09a 50%,#a8403a)" role="img" aria-label="Photo of a mother and child riding bicycles in a park"></div>
    <div class="date" style="left:118px;top:24px">APRI 17<br>2021</div>
    <div class="news-head abs" style="left:198px;top:20px;width:190px">Nemo enim ipsam voluptatem quiasit</div>
    <p class="news-body abs" style="left:200px;top:80px;width:180px">Sed ut perspiciatis unde omnis iste natus error sit voluptatem accusantium doloremque</p>
    <div class="more abs" style="left:200px;top:140px">LEARN MORE <svg width="14" height="10" viewBox="0 0 14 10"><path d="M1 5h11M8 1l4 4-4 4" stroke="#a3060e" stroke-width="2" fill="none"/></svg></div>
  </div>
  <div class="card" style="left:651px;top:2513px;width:402px;height:184px">
    <div class="abs" style="left:0;top:0;width:171px;height:184px;background:linear-gradient(135deg,#6f8a4a,#4a6aa0 50%,#8a9a5a)" role="img" aria-label="Photo of a father sitting on grass with his son on his shoulders"></div>
    <div class="date" style="left:118px;top:24px">APRI 17<br>2021</div>
    <div class="news-head abs" style="left:198px;top:20px;width:190px">Nemo enim ipsam voluptatem quiasit</div>
    <p class="news-body abs" style="left:200px;top:80px;width:180px">Sed ut perspiciatis unde omnis iste natus error sit voluptatem accusantium doloremque</p>
    <div class="more abs" style="left:200px;top:140px">LEARN MORE <svg width="14" height="10" viewBox="0 0 14 10"><path d="M1 5h11M8 1l4 4-4 4" stroke="#a3060e" stroke-width="2" fill="none"/></svg></div>
  </div>

  <div class="abs bp-photo" role="img" aria-label="Photo of a young family sitting together on the grass in a park"></div>
  <div class="abs bp-card">
    <h2>BIRTH PARENT<br>SEARCHING</h2>
    <p>Sed ut perspiciatis unde omnis iste natus voluptatem accusantium doloremque laudantium, totam rem aperiam, eaque ipsa quae ab illo inventore veritatis et quasi architecto beatae vitae dicta sunt explicabo. Nemo enim ipsam voluptatem quia voluptas sit aspnatur aut odit aut fugit, sed quia consequuntur</p>
    <div class="btn btn-red" style="left:34px;top:269px;width:160px;height:42px">Learn More</div>
  </div>

  <div class="abs clients"></div>
  <h2 class="abs section-title" style="top:3404px">WHAT OUR CLIENTS SAY!</h2>

  <div class="quote" style="left:166px;top:3497px">
    <svg class="abs" style="left:40px;top:32px" width="40" height="28" viewBox="0 0 40 28"><path d="M2 26V14C2 6 6 2 14 2v6c-4 0-6 2-6 6h6v12zM22 26V14c0-8 4-12 12-12v6c-4 0-6 2-6 6h6v12z" fill="#e4e4ec"/></svg>
    <p>Sed ut perspiciatis unde omnis iste natus error sit voluptatem accntium doloremque launtium, totam rem aperiam, eaque ipsa quae ab illo intore veritatis et quasi architecto beatae vitae dicta sunt explicabo. Nemo enim ipsam votatem quia voluptas sit aspernatur aut odit aut fugit,</p>
    <div class="stars">★★★★★</div>
  </div>
  <svg class="abs" style="left:465px;top:3742px" width="70" height="46" viewBox="0 0 70 46"><path d="M0 0h70L8 46z" fill="#fff"/></svg>
  <div class="avatar" style="left:224px;top:3773px" role="img" aria-label="Portrait of a client"></div>
  <div class="person" style="left:328px;top:3795px">JOHN DOE<br>TULO LINK</div>

  <div class="quote" style="left:621px;top:3497px">
    <svg class="abs" style="left:40px;top:32px" width="40" height="28" viewBox="0 0 40 28"><path d="M2 26V14C2 6 6 2 14 2v6c-4 0-6 2-6 6h6v12zM22 26V14c0-8 4-12 12-12v6c-4 0-6 2-6 6h6v12z" fill="#e4e4ec"/></svg>
    <p>Sed ut perspiciatis unde omnis iste natus error sit voluptatem accntium doloremque launtium, totam rem aperiam, eaque ipsa quae ab illo intore veritatis et quasi architecto beatae vitae dicta sunt explicabo. Nemo enim ipsam votatem quia voluptas sit aspernatur aut odit aut fugit,</p>
    <div class="stars">★★★★★</div>
  </div>
  <svg class="abs" style="left:920px;top:3742px" width="70" height="46" viewBox="0 0 70 46"><path d="M0 0h70L8 46z" fill="#fff"/></svg>
  <div class="avatar" style="left:672px;top:3773px" role="img" aria-label="Portrait of a client"></div>
  <div class="person" style="left:776px;top:3795px">JOHN DOE<br>TULO LINK</div>

  <svg class="slider-arrow" style="left:158px;top:3610px" width="20" height="20" viewBox="0 0 20 20"><path d="M13 3l-7 7 7 7" stroke="#222" stroke-width="2" fill="none"/></svg>
  <svg class="slider-arrow" style="left:1022px;top:3610px" width="20" height="20" viewBox="0 0 20 20"><path d="M7 3l7 7-7 7" stroke="#222" stroke-width="2" fill="none"/></svg>

  <div class="abs join-photo" role="img" aria-label="Red-tinted photo of a young child's face"></div>
  <svg class="abs" style="left:0;top:3925px" width="1200" height="90" viewBox="0 0 1200 90">
    <path d="M0,0 H1200 V88 C1000,20 700,0 400,18 C250,28 100,40 0,44 Z" fill="#f3f3f3"/>
    <path d="M0,44 C100,40 250,28 400,18 C700,0 1000,20 1200,88" stroke="#333" stroke-width="4" fill="none"/>
  </svg>
  <h2 class="abs join-title">JOIN THE COMMUNITY! GET EMAIL UPDATES</h2>
  <div class="field" style="left:233px;top:4155px;width:358px">First Name</div>
  <div class="field" style="left:608px;top:4155px;width:359px">Last Name</div>
  <div class="field" style="left:233px;top:4217px;width:581px">Email address</div>
  <div class="btn btn-white" style="left:813px;top:4217px;width:154px;height:45px;font-size:16px">Submit</div>

  <div class="contact-col" style="left:180px;width:285px">
    <svg width="60" height="60" viewBox="0 0 60 60"><circle cx="30" cy="30" r="28" fill="none" stroke="#a3060e" stroke-width="2.5"/><path d="M30 16a9 9 0 00-9 9c0 7 9 18 9 18s9-11 9-18a9 9 0 00-9-9z" fill="#a3060e"/><circle cx="30" cy="25" r="3.5" fill="#fff"/></svg>
    <h4>ADDRESS</h4>
    <p>520 enim ipsam voluptatem quia<br>voluptas sit</p>
  </div>
  <div class="divider" style="left:498px"></div>
  <div class="contact-col" style="left:470px;width:270px">
    <svg width="60" height="60" viewBox="0 0 60 60"><circle cx="30" cy="30" r="28" fill="none" stroke="#a3060e" stroke-width="2.5"/><circle cx="30" cy="30" r="15" fill="#a3060e"/><path d="M24 22c1-1 3-1 3 1l1 3-2 2c1 2 3 4 5 5l2-2 3 1c2 0 2 2 1 3-2 2-5 2-8 0-3-2-5-4-6-7-1-3 0-5 1-6z" fill="#fff"/></svg>
    <h4>PHONE</h4>
    <p>800.555.0142</p>
  </div>
  <div class="divider" style="left:729px"></div>
  <div class="contact-col" style="left:760px;width:260px">
    <svg width="60" height="60" viewBox="0 0 60 60"><circle cx="30" cy="30" r="28" fill="none" stroke="#a3060e" stroke-width="2.5"/><circle cx="30" cy="30" r="15" fill="#a3060e"/><rect x="21" y="24" width="18" height="13" rx="1.5" fill="#fff"/><path d="M21 25l9 7 9-7" stroke="#a3060e" stroke-width="1.6" fill="none"/></svg>
    <h4>EMAIL</h4>
    <p>info@tulolink.org</p>
  </div>
  <div class="abs" style="left:143px;top:4585px;width:912px;height:1px;background:#ccc"></div>
  <p class="abs footer-links">Home &nbsp;|&nbsp; Mission &nbsp;|&nbsp; Vision &nbsp;|&nbsp; About Us &nbsp;|&nbsp; Donations &nbsp;|&nbsp; Blog &nbsp;|&nbsp; Contact</p>
  <p class="abs copyright">Tulo Link © 2021 All Rights Reserved | Privacy policy</p>
  <div class="social" style="left:534px" aria-label="Social profile"></div>
  <div class="social" style="left:583px" aria-label="Social profile"></div>
  <div class="social" style="left:632px" aria-label="Social profile"></div>
</div>
</body>
</html>
```